Falcon Letterhead

Looking for a design template for our company’s official letterheads & business cards.It has to be mainly white and include our company logo, website, social media handle, address, phone number. Visit our website to have an idea of our brand identity and colours. Please use the same font that we are using in our website.
Target Market(s)
Lubricants & Greases, Industrial markets, Automotive
Font styles to use
Other font styles liked:
- Saira Extra-Condensed
Colors
ffffff
000000
fbee3f
Requirements
Must have
- It must be consistent with our brand identity. It must use the same exact yellow (Pantone color: 102C) and black (Pantone color: K100) as our brand colors.
- Must also use our font attached (Saira.zip). It's called Saira Extra-Condensed.
- We intend to use the FALCON logo and not the small mini-FN logo.
- On the design we must include ALL of the following:
- E-mail: info@falconoils.example
- @FalconGreases
- www.falconoils.example
- Address: P.O. Boc 4728, Qurain 53004, Kuwait
- Phone: (+965) 24718395
- Gulf Marwa Oils logo (attached). The logo attached is in Blue/Red but you can select one solid color for all of it such as BLACK or YELLOW depending on what background color you'll select.
Nice to have
- Like it to be as professional and as modern as possible. It has look clean, slick and classy.
Should not have
- Too many different colors.

```html
<!DOCTYPE html>
<html lang="en">
<head>
<meta charset="utf-8">
<title>Falcon Stationery</title>
<link href="https://fonts.googleapis.com/css2?family=Saira+Extra+Condensed:wght@700&family=Roboto:wght@400;500;700&family=Questrial&display=swap" rel="stylesheet">
<style>
  :root {
    --bg: #dcdcdc;
    --ink: #231f20;
    --yellow: #f0e010;
    --paper: #f7f7f7;
    --text-grey: #4a4a4a;
    --card-text: #ffffff;
  }
  * { margin: 0; padding: 0; box-sizing: border-box; }
  html, body { width: 1200px; height: 877px; overflow: hidden; background: var(--bg); }
  .canvas { position: relative; width: 1200px; height: 877px; }

  .wordmark { position: absolute; display: block; overflow: visible; }
  .wordmark text {
    font-family: "Saira Extra Condensed", sans-serif;
    font-weight: 700;
  }

  /* Dark business card */
  .card-front {
    position: absolute; left: 82px; top: 158px; width: 449px; height: 257px;
    background: var(--ink); color: var(--card-text);
    font-family: "Roboto", sans-serif;
  }
  .card-front .wordmark { left: 66px; top: 98px; width: 148px; height: 60px; }
  .card-front .wordmark text { fill: var(--yellow); }
  .card-front .divider {
    position: absolute; left: 243px; top: 58px; width: 1px; height: 136px;
    background: linear-gradient(to bottom, transparent, #9a9a9a 50%, transparent);
  }
  .card-details { position: absolute; left: 268px; top: 62px; white-space: nowrap; }
  .card-details .person-name { color: var(--yellow); font-weight: 700; font-size: 17px; line-height: 20px; }
  .card-details .person-role { font-weight: 500; font-size: 11.5px; line-height: 14px; }
  .card-details .address { margin-top: 8px; font-size: 11.5px; line-height: 14px; }
  .contact-list { list-style: none; margin-top: 7px; font-size: 11.5px; line-height: 14.3px; }
  .contact-list li { display: flex; align-items: center; gap: 7px; }
  .contact-list svg { width: 10px; height: 10px; flex: none; }

  /* Yellow business card */
  .card-back {
    position: absolute; left: 82px; top: 456px; width: 449px; height: 257px;
    background: var(--yellow); color: var(--ink);
  }
  .card-back .wordmark { left: 130px; top: 94px; width: 189px; height: 70px; }
  .card-back .wordmark text { fill: var(--ink); }
  .card-back .site {
    position: absolute; left: 0; right: 0; top: 214px; text-align: center;
    font-family: "Roboto", sans-serif; font-size: 10.5px; letter-spacing: 6px;
    color: var(--ink);
  }

  /* Letterhead */
  .letterhead {
    position: absolute; left: 594px; top: 64px; width: 527px; height: 742px;
    background: var(--paper); box-shadow: 0 0 6px rgba(0,0,0,0.12);
    font-family: "Questrial", sans-serif; color: var(--text-grey);
  }
  .letterhead .wordmark { left: 46px; top: 59px; width: 108px; height: 48px; }
  .letterhead .wordmark text { fill: var(--ink); }
  .letter-contact {
    position: absolute; left: 390px; top: 52px; padding-left: 9px;
    border-left: 1px solid #d6d6d6; font-size: 7.3px; line-height: 10.5px; white-space: nowrap;
  }
  .letter-contact .contact-list { margin-top: 5px; font-size: 7.3px; line-height: 10.5px; }
  .letter-contact .contact-list li { gap: 5px; }
  .letter-contact .contact-list svg { width: 7px; height: 7px; }
  .letter-body { position: absolute; left: 46px; top: 212px; width: 438px; }
  .salutation { font-size: 13.5px; margin-bottom: 25px; color: #444; }
  .letter-body p { font-size: 7.4px; line-height: 11.4px; text-align: justify; margin-bottom: 11.4px; }
  .letter-body .closing { margin-top: 22px; }
  .signature { position: absolute; left: 42px; top: 520px; width: 92px; height: 36px;
    background: linear-gradient(90deg, rgba(47,95,168,0.18), rgba(47,95,168,0.06)); border-radius: 3px; }
</style>
</head>
<body>
<div class="canvas">

  <section class="card-front">
    <svg class="wordmark" viewBox="0 0 148 60" width="148" height="60">
      <text x="0" y="57" font-size="76" textLength="148" lengthAdjust="spacingAndGlyphs">FALCON</text>
    </svg>
    <div class="divider"></div>
    <div class="card-details">
      <div class="person-name">OMAR HADDAD</div>
      <div class="person-role">CEO/FOUNDER</div>
      <div class="address">P.O. Boc 4728,<br>Qurain 53004, Kuwait</div>
      <ul class="contact-list">
        <li><svg viewBox="0 0 10 10"><path d="M2 0.5 L3.8 2.8 L2.8 4 Q4 6.2 6 7.2 L7.2 6.2 L9.5 8 L8.2 9.5 Q3.5 9 0.5 1.8 Z" fill="var(--yellow)"/></svg>(+965) 24718395</li>
        <li><svg viewBox="0 0 10 10"><rect x="0.5" y="2" width="9" height="6.5" fill="var(--yellow)"/><path d="M0.5 2 L5 5.8 L9.5 2" stroke="var(--ink)" stroke-width="0.9" fill="none"/></svg>info@falconoils.example</li>
        <li><svg viewBox="0 0 10 10"><circle cx="5" cy="5" r="4.5" fill="var(--yellow)"/><path d="M3 3 Q5 4 4 6 M6 2 Q7 5 6.5 8" stroke="var(--ink)" stroke-width="0.9" fill="none"/></svg>www.falconoils.example</li>
        <li><svg viewBox="0 0 10 10"><circle cx="5" cy="5" r="4.5" fill="var(--yellow)"/></svg>@FalconGreases</li>
      </ul>
    </div>
  </section>

  <section class="card-back">
    <svg class="wordmark" viewBox="0 0 189 70" width="189" height="70">
      <text x="0" y="67" font-size="90" textLength="189" lengthAdjust="spacingAndGlyphs">FALCON</text>
    </svg>
    <div class="site">www.falconoils.example</div>
  </section>

  <section class="letterhead">
    <svg class="wordmark" viewBox="0 0 108 48" width="108" height="48">
      <text x="0" y="46" font-size="61" textLength="108" lengthAdjust="spacingAndGlyphs">FALCON</text>
    </svg>
    <div class="letter-contact">
      <div>P.O. Boc 4728,<br>Qurain 53004, Kuwait</div>
      <ul class="contact-list">
        <li><svg viewBox="0 0 10 10"><path d="M2 0.5 L3.8 2.8 L2.8 4 Q4 6.2 6 7.2 L7.2 6.2 L9.5 8 L8.2 9.5 Q3.5 9 0.5 1.8 Z" fill="var(--ink)"/></svg>(+965) 24718395</li>
        <li><svg viewBox="0 0 10 10"><rect x="0.5" y="2" width="9" height="6.5" fill="var(--ink)"/><path d="M0.5 2 L5 5.8 L9.5 2" stroke="var(--paper)" stroke-width="0.9" fill="none"/></svg>info@falconoils.example</li>
        <li><svg viewBox="0 0 10 10"><circle cx="5" cy="5" r="4.5" fill="var(--ink)"/><path d="M3 3 Q5 4 4 6 M6 2 Q7 5 6.5 8" stroke="var(--paper)" stroke-width="0.9" fill="none"/></svg>www.falconoils.example</li>
        <li><svg viewBox="0 0 10 10"><circle cx="5" cy="5" r="4.5" fill="var(--ink)"/></svg>@FalconGreases</li>
      </ul>
    </div>

    <div class="letter-body">
      <div class="salutation">Dear Mr. Haddad,</div>
      <p>Lorem ipsum dolor sit amet, consectetur adipiscing elit. Donec orci purus, luctus vitae dignissim eu, iaculis sed purus. Vivamus faucibus, ipsum nec aliquet viverra, leo mauris condimentum ligula, sit amet sagittis enim ligula quis arcu. Nam egestas tortor id nisi porttitor mattis. In tortor ante, ultricies in suscipit a, tempus non massa. Vivamus et auctor mi. Fusce vel massa nulla. Phasellus nec eros mauris, et scelerisque orci.</p>
      <p>Donec malesuada orci vitae nulla accumsan porta a id massa. Quisque accumsan iaculis magna sit amet fringilla. Maecenas consequat, magna eget tincidunt semper, odio nibh rutrum mi, id feugiat ante nisi eu risus. Vestibulum nunc orci, rhoncus a placerat in, ultricies in mi. Cras mattis varius eros, vel fringilla nisi suscipit eget. Quisque scelerisque sagittis nulla at porttitor.</p>
      <p>Sed id augue vitae urna euismod commodo aliquet a quam. Pellentesque arcu velit, cursus et malesuada ut, consequat et diam. Nullam erat sem, rhoncus id ullamcorper vitae, rhoncus et arcu. In ultricies ultricies nulla, ut rutrum nisi iaculis at. Donec eu magna a metus ornare faucibus. Fusce aliquet faucibus ultricies. Morbi semper, est id tincidunt gravida, sem arcu adipiscing lacus, ac bibendum nulla leo eu purus. Quisque nec diam sed risus consectetur a ccumsan quis quis nibh. Vestibulum id purus lorem.</p>
      <p>It is a long established fact that a reader will be distracted by the readable content of a page when looking at its layout. The point of using Lorem Ipsum is that it has a more-or-less normal distribution of letters, as opposed to using 'Content here, content here', making it look like readable English. Many desktop publishing packages</p>
      <p class="closing">Sincerely,</p>
    </div>
    <div class="signature" role="img" aria-label="Handwritten signature of Omar Haddad in blue ink"></div>
  </section>

</div>
</body>
</html>
```